From Portrait to Landscape

Take a PPT document made of 54 slide of graphs, images and text and change the orientation of each one of the 54 slides from the existing Portrait layout to the Landscape one.
All the graphics and texts (including text formatting, commas, bullet points etc.) must be kept the same but spaces are reorganized in the new Landscape orientation favoring the size of the graphs (possibily reducing the text areas).
Please, find attached the first 10 pages of the PPT document (for now, in PDF format) and a couple of sample pages of the PPT.x\

Target Market(s)

Readers of the Report (ecommerce players in Italy)

Requirements
Must have
• Graphics should be larger in the Landscape orientation than they are now in the Poirtrait one

```html
<!DOCTYPE html>
<html lang="it">
<head>
<meta charset="utf-8">
<title>Gli acquisti online da Smartphone</title>
<link href="https://fonts.googleapis.com/css2?family=Alegreya+Sans:wght@300;400;500;700&display=swap" rel="stylesheet">
<style>
  :root{
    --blue:#2553a2;
    --blue-dark:#1f4e9b;
    --grey-text:#6b6b6b;
    --dark-text:#4a4a4a;
    --bar-grey:#c4c4c4;
    --overlay-grey:#9aa1b5;
    --panel:#ebebeb;
    --rule:#e2e2e2;
    --magenta:#a3195b;
    --venn-grey:#9b9b9b;
  }
  *{margin:0;padding:0;box-sizing:border-box}
  html,body{width:1200px;height:675px;overflow:hidden;background:#fff}
  body{font-family:"Alegreya Sans",sans-serif;color:var(--grey-text)}
  .slide{position:relative;width:1200px;height:675px}
  .abs{position:absolute}
  .title{left:110px;top:50px;font-size:33px;font-weight:700;color:var(--blue);letter-spacing:-0.5px;line-height:1}
  .title-rule{left:110px;top:93px;width:983px;height:3px;background:var(--blue)}
  .subtitle{left:110px;top:101px;font-size:27px;font-weight:400;color:var(--blue);line-height:1.2}
  .intro,.conclusion{font-size:14px;line-height:16.3px;text-align:justify;color:var(--grey-text)}
  .intro{left:110px;top:161px;width:463px}
  .conclusion{left:628px;top:420px;width:463px}
  svg text{font-family:"Alegreya Sans",sans-serif}
  .caption{background:var(--panel);color:var(--dark-text);font-size:11.5px;line-height:13.5px;text-align:center;display:flex;align-items:center;justify-content:center}
  .note{left:414px;width:159px;background:var(--panel)}
  .note-head{background:var(--blue);color:#fff;font-size:11.5px;font-weight:500;text-align:center;height:19px;line-height:19px}
  .note-body{color:var(--dark-text);font-size:11px;line-height:13.5px;text-align:center;padding:3px 6px}
  .venn-legend{left:952px;font-size:12px;font-weight:500;display:flex;align-items:center;gap:6px}
  .venn-legend i{display:inline-block;width:11px;height:11px}
  .footer{left:108px;top:603px;width:985px;height:30px;background:var(--blue-dark);border-radius:12px 14px 12px 10px;color:#fff}
  .footer-name{position:absolute;left:29px;top:3px;font-size:21px}
  .footer-page{position:absolute;right:20px;top:2px;font-size:20px}
</style>
</head>
<body>
<div class="slide">
  <h1 class="abs title">GLI ACQUISTI ONLINE DA SMARTPHONE</h1>
  <div class="abs title-rule"></div>
  <h2 class="abs subtitle">Confronto con tutti gli acquisti online</h2>

  <p class="abs intro">Gli acquisti online da Smartphone, sia su Web che su App, sono generati da un segmento di acquirenti online più attivo della media. Fino a tre anni fa l’incidenza del segmento di acquirenti da Smartphone aveva caratteristiche peculiari, sia di profilo che di comportamento. Negli ultimi anni l’estensione di questo segmento è cresciuta a dal punto da renderlo quasi indistinguibile rispetto al totale degli acquirenti online.</p>

  <!-- Category chart -->
  <svg class="abs" style="left:100px;top:296px" width="310" height="245" viewBox="0 0 310 245">
    <g stroke="var(--rule)" stroke-width="1">
      <line x1="153" y1="5" x2="299" y2="5"/><line x1="153" y1="19" x2="299" y2="19"/><line x1="153" y1="33" x2="299" y2="33"/><line x1="153" y1="48" x2="299" y2="48"/><line x1="153" y1="62" x2="299" y2="62"/><line x1="153" y1="76" x2="299" y2="76"/><line x1="153" y1="90" x2="299" y2="90"/><line x1="153" y1="105" x2="299" y2="105"/><line x1="153" y1="119" x2="299" y2="119"/><line x1="153" y1="133" x2="299" y2="133"/><line x1="153" y1="147" x2="299" y2="147"/><line x1="153" y1="162" x2="299" y2="162"/><line x1="153" y1="176" x2="299" y2="176"/><line x1="153" y1="190" x2="299" y2="190"/><line x1="153" y1="205" x2="299" y2="205"/>
    </g>
    <g font-size="9.5" fill="var(--dark-text)" text-anchor="end">
      <text x="147" y="16">Food delivery</text><text x="147" y="30">Attrezzatura sportiva</text><text x="147" y="44">Elettrodomestici</text><text x="147" y="58">Salute &amp; Benessere</text><text x="147" y="73">Computer e Tablet</text><text x="147" y="87">Contenuti digitali</text><text x="147" y="101">Spesa alimentare/ casa</text><text x="147" y="115">Abbigliamento (non scarpe)</text><text x="147" y="130">Cosmetici e profumeria</text><text x="147" y="144">Arredamento e casalinghi</text><text x="147" y="158">Scarpe</text><text x="147" y="172">Gioielli, bijoux, orologi</text><text x="147" y="187">Contenuti fisici (Libri, CD, DVD)</text><text x="147" y="201">Software e servizi online</text><text x="147" y="215">Elettronica (non PC, Tablet, Phone)</text>
    </g>
    <g fill="var(--blue)">
      <rect x="153" y="8" width="94.4" height="8"/><rect x="153" y="22" width="53" height="8"/><rect x="153" y="36" width="59" height="8"/><rect x="153" y="51" width="100.4" height="8"/><rect x="153" y="65" width="27.6" height="8"/><rect x="153" y="79" width="70.5" height="8"/><rect x="153" y="93" width="97.1" height="8"/><rect x="153" y="108" width="122.2" height="8"/><rect x="153" y="122" width="91.4" height="8"/><rect x="153" y="136" width="66" height="8"/><rect x="153" y="150" width="96.9" height="8"/><rect x="153" y="165" width="50.5" height="8"/><rect x="153" y="179" width="82.6" height="8"/><rect x="153" y="193" width="36.9" height="8"/><rect x="153" y="208" width="83.3" height="8"/>
    </g>
    <g fill="var(--overlay-grey)">
      <rect x="153" y="11" width="31" height="5"/><rect x="153" y="25" width="31" height="5"/><rect x="153" y="39" width="38" height="5"/><rect x="153" y="54" width="67" height="5"/><rect x="153" y="68" width="19" height="5"/><rect x="153" y="82" width="49" height="5"/><rect x="153" y="96" width="67" height="5"/><rect x="153" y="111" width="88" height="5"/><rect x="153" y="125" width="69" height="5"/><rect x="153" y="139" width="51" height="5"/><rect x="153" y="153" width="75" height="5"/><rect x="153" y="168" width="39" height="5"/><rect x="153" y="182" width="65" height="5"/><rect x="153" y="196" width="31" height="5"/><rect x="153" y="211" width="72" height="5"/>
    </g>
    <g font-size="8.5" fill="var(--blue-dark)" font-weight="500">
      <text x="259" y="16">37.6%</text><text x="212" y="30">21.1%</text><text x="218" y="44">23.5%</text><text x="259" y="58">40.0%</text><text x="186" y="73">11.0%</text><text x="229" y="87">28.1%</text><text x="256" y="101">38.7%</text><text x="281" y="115">48.7%</text><text x="250" y="130">36.4%</text><text x="225" y="144">26.3%</text><text x="256" y="158">38.6%</text><text x="209" y="172">20.1%</text><text x="241" y="187">32.9%</text><text x="196" y="201">14.7%</text><text x="242" y="215">33.2%</text>
    </g>
    <g font-size="10.5">
      <rect x="32" y="229" width="6" height="6" fill="var(--blue)"/><text x="40" y="236" fill="var(--dark-text)">Acquirenti da smartphone</text>
      <rect x="170" y="229" width="6" height="6" fill="var(--bar-grey)"/><text x="178" y="236" fill="var(--dark-text)">Tutti gli acquirenti online</text>
    </g>
  </svg>
  <div class="abs caption" style="left:118px;top:541px;width:281px;height:36px">Categorie di prodotti e servizi a maggior incidenza di<br>acquirenti da Smartphone rispetto alla media</div>

  <div class="abs note" style="top:302px;height:67px">
    <div class="note-head">Gli acquisti da Smartphone</div>
    <div class="note-body">Le categorie più affini all’acquisto da Smartphone sono elencate qui a sinistra</div>
  </div>
  <div class="abs note" style="top:375px;height:105px">
    <div class="note-head">Concentrazione non elevata</div>
    <div class="note-body">Le categorie con la minor incidenza di acquirenti da Smartphone sono l’enogastronomia, i Soggiorni di vacanza, le Assicurazioni e i biglietti per eventi</div>
  </div>
  <div class="abs note" style="top:487px;height:90px">
    <div class="note-head">Prodotti e servizi</div>
    <div class="note-body">L’acquisto da smartphone riproduce lo stesso rapporto tra prodotti e servizi e beni digitali che si nota per il totale degli acquisti online</div>
  </div>

  <!-- Merchant chart -->
  <svg class="abs" style="left:620px;top:160px" width="300" height="190" viewBox="0 0 300 190">
    <g stroke="var(--rule)"><line x1="58" y1="4" x2="296" y2="4"/><line x1="58" y1="27" x2="296" y2="27"/><line x1="58" y1="50" x2="296" y2="50"/><line x1="58" y1="74" x2="296" y2="74"/><line x1="58" y1="97" x2="296" y2="97"/><line x1="58" y1="120" x2="296" y2="120"/><line x1="58" y1="144" x2="296" y2="144"/><line x1="58" y1="167" x2="296" y2="167"/></g>
    <g font-size="9.5" fill="var(--dark-text)" text-anchor="end">
      <text x="94" y="19">eRetailer</text><text x="94" y="42">Produttore</text><text x="94" y="66">Retailer tradizionale</text><text x="94" y="89">Marketplace</text><text x="94" y="112">Coupon</text><text x="94" y="135">Comparatore</text><text x="94" y="159">Vendite Private</text>
    </g>
    <g fill="var(--blue)"><rect x="99" y="6" width="181.7" height="8"/><rect x="99" y="29" width="38.2" height="8"/><rect x="99" y="53" width="33.1" height="8"/><rect x="99" y="76" width="12.5" height="8"/><rect x="99" y="99" width="5.1" height="8"/><rect x="99" y="122" width="11.9" height="8"/><rect x="99" y="146" width="1.2" height="8"/></g>
    <g fill="var(--bar-grey)"><rect x="99" y="16" width="183.4" height="8"/><rect x="99" y="39" width="37.4" height="8"/><rect x="99" y="63" width="33.7" height="8"/><rect x="99" y="86" width="12.2" height="8"/><rect x="99" y="109" width="6.2" height="8"/><rect x="99" y="132" width="9.6" height="8"/><rect x="99" y="156" width="1.2" height="8"/></g>
    <g font-size="8.5" font-weight="500" fill="var(--blue-dark)">
      <text x="274" y="13" text-anchor="end" fill="#fff">64.2%</text><text x="142" y="36">13.5%</text><text x="137" y="60">11.7%</text><text x="116" y="83">4.4%</text><text x="109" y="106">1.8%</text><text x="116" y="129">4.2%</text><text x="105" y="153">0.2%</text>
    </g>
    <g font-size="8.5" fill="var(--grey-text)">
      <text x="274" y="23" text-anchor="end">64.8%</text><text x="142" y="46">13.2%</text><text x="137" y="70">11.9%</text><text x="116" y="93">4.3%</text><text x="111" y="116">2.2%</text><text x="113" y="139">3.4%</text><text x="105" y="163">0.2%</text>
    </g>
    <g font-size="11">
      <rect x="20" y="177" width="6" height="6" fill="var(--blue)"/><text x="29" y="184" fill="var(--dark-text)">Acquirenti da smartphone</text>
      <rect x="163" y="177" width="6" height="6" fill="var(--bar-grey)"/><text x="172" y="184" fill="var(--dark-text)">Tutti gli acquirenti online</text>
    </g>
  </svg>
  <div class="abs caption" style="left:629px;top:354px;width:289px;height:32px">Tipologie di merchant utilizzati dagli acquirenti da<br>Smartphone rispetto a tutti gli acquirenti online</div>

  <!-- Overlap diagram -->
  <div class="abs venn-legend" style="top:175px;color:var(--dark-text)"><i style="background:var(--venn-grey)"></i>Prodotti fisici</div>
  <div class="abs venn-legend" style="top:199px;color:var(--magenta)"><i style="background:var(--magenta)"></i>Beni digitali e servizi</div>
  <svg class="abs" style="left:920px;top:220px" width="180" height="112" viewBox="0 0 180 112">
    <ellipse cx="89" cy="50" rx="81" ry="45" fill="var(--venn-grey)" stroke="#7c7c7c" stroke-width="1"/>
    <ellipse cx="89" cy="73" rx="81" ry="36" fill="#b54d7f" fill-opacity="0.85" stroke="var(--magenta)" stroke-width="1.5"/>
    <g font-size="13" fill="#fff" text-anchor="middle"><text x="89" y="24">42,3%</text><text x="89" y="63">57,0%</text><text x="89" y="106">0,7%</text></g>
  </svg>
  <div class="abs caption" style="left:928px;top:338px;width:163px;height:48px">Gli acquirenti online di prodotti e di servizi e beni digitali sono notevolmente sovrapposti</div>

  <p class="abs conclusion">La tipologia di merchant ai quali si rivolgono gli acquirenti da Smartphone è simile alla media e le differenze non superano il punto percentuale. In definitiva, si può affermare che l’acquisto via Smartphone è più comune in certe categorie di prodotti e servizi ma simile per tipologia di servizio dei merchant interessati.</p>

  <footer class="abs footer">
    <span class="footer-name">Web Commerce -&nbsp; Aprile 2022</span>
    <span class="footer-page">33</span>
  </footer>
</div>
</body>
</html>
```